Tuition Center Website

We need a new web site for a tutoring company based in sydney.

We only teach senior highschool students and pride ourselves on building the students abilities to think their way through life.

I would like a bright and vibrant website that looks professional and modern.
It needs to look simple and neat but also have the functionality we need.
Images and flash would be good.

Please keep in mind that the site must be appealing to a younger audience.

We need a multipage website with the following navigation bars:

1.Home (As logo not "home" button)
I would like a news box/ticker somewhere that can stream our chatterbook and flitter feeds and also any news updates we want to put up.
Subscribe to newsletter button.

2. About us.
This needs to be a pull down into:
-What we do
-Why we do it
-How we do it

3. Courses
Pulldown into:
-Maths
-English
-Science
(we may need to attach extra pages behind these e.g. Courses/Science/Physics or Courses/Science/Chemistry and possibly add a link to a new quizzo form)

4. Inspired
This page is like a blog page where we can upload videos, links to articles that we find to be inspiring and hopefully will inspire others.

5. Inspire
This is a recruitment page. Only content here.

6. Contact us.
Mapzy map widget and a 'contact us' form

* Our branding requires green close to #12FF3D

***Please have a look at the current website.
@ www.brindlelearning.com.au

Thanks everybody hope the revision of my brief is better and more informative than my last one

Target Market(s)

senior highschool students aged 15-19, parents ( to a lesser degree)

Industry/Entity Type

It Company

Requirements
Must have
• Ability to change content on pages.

The green doesn't have to be everywhere, but it must be obvious that it is our colour.

Nice to have
• Sites with a nicer mix of images and flash will be given more consideration. But then again, if you amaze us, you amaze us and we will go with your design.
Should not have
• Should stay away from ocre, brown colours and serif fonts.

```html
<!DOCTYPE html>
<html lang="en">
<head>
<meta charset="utf-8">
<title>Brindle Learning – HSC coaching &amp; mentoring</title>
<link rel="stylesheet" href="https://fonts.googleapis.com/css2?family=Noto+Sans:ital,wght@0,400;0,700;1,400&family=Cabin+Sketch:wght@700&family=Patrick+Hand&family=Sniglet:wght@400;800&display=swap">
<style>
:root{
  --green:#4a9a12;
  --green-bright:#4fae0c;
  --green-panel:#56a71b;
  --green-pale:#e6f3d9;
  --green-pale-border:#b9d9a0;
  --charcoal:#403b3b;
  --ink:#333;
  --muted:#555;
  --line:#d6d6d6;
  --white:#fff;
}
*{margin:0;padding:0;box-sizing:border-box}
html,body{width:1059px;height:1200px;overflow:hidden;background:var(--white)}
body{font-family:"Noto Sans",sans-serif;color:var(--ink)}
h1,h2,h3{font-weight:400}
.page{position:relative;width:1000px;height:1133px;transform:scale(1.059);transform-origin:0 0;
  background:linear-gradient(#fff 0,#f3f3f3 150px,#e9e9e9 495px,#fff 495px)}
.abs{position:absolute}

/* header */
.brand{left:32px;top:60px;display:flex;align-items:center;gap:10px}
.brand-mark{width:22px;height:22px;background:var(--green-bright)}
.brand-name{font-size:24px;font-weight:700;color:var(--green-bright);line-height:1.05;width:130px}
.contact{top:12px;display:flex;align-items:center;gap:8px;font-size:14px;color:var(--green);white-space:nowrap}
.contact-phone{left:517px}
.contact-mail{left:660px}
.search{left:738px;top:66px;display:flex;height:27px}
.search-field{width:160px;border:1px solid #d4d4d4;border-right:none;background:#f6f6f6;border-radius:3px 0 0 3px;display:flex;align-items:center;gap:10px;padding-left:12px;font-size:14px;color:#aaa}
.search-button{width:66px;background:var(--charcoal);color:#fff;font-size:13px;font-weight:700;display:flex;align-items:center;justify-content:center;border-radius:0 3px 3px 0}
.main-nav{left:210px;top:102px;width:760px;height:45px;background:var(--charcoal);border-radius:3px;display:flex}
.main-nav a{color:#fff;text-decoration:none;font-size:15px;display:flex;align-items:center;justify-content:center;border-right:1px solid #5a5454}
.main-nav a:last-child{border-right:none}

/* hero */
.hero-photo{left:20px;top:195px;width:445px;height:300px;
  background:radial-gradient(ellipse at 45% 55%,#3a8fc9 0,#6a8aa0 25%,#b9b4ae 50%,rgba(233,233,233,0) 78%)}
.tagline{left:500px;top:228px;font-family:"Patrick Hand",sans-serif;font-size:22px;color:#333;letter-spacing:1px;white-space:nowrap}
.headline{left:500px;top:262px;font-family:"Cabin Sketch",sans-serif;font-weight:700;font-size:38px;color:var(--green-bright);white-space:nowrap}
.btn{top:332px;height:41px;border-radius:3px;display:flex;align-items:center;font-family:"Sniglet",sans-serif;font-size:16px;white-space:nowrap;box-shadow:0 1px 2px rgba(0,0,0,.25);text-decoration:none}
.btn-courses{left:497px;width:215px;background:var(--green-bright);color:#fff;padding:0 10px;justify-content:space-between}
.btn-trial{left:726px;width:221px;background:var(--green-pale);border:1px solid var(--green-pale-border);color:var(--green);padding-left:12px}
.btn-trial .divider{margin-left:auto;height:27px;border-left:1px solid var(--green-pale-border);padding:0 9px;display:flex;align-items:center}

/* welcome band */
.welcome-band{left:0;top:494px;width:1000px;height:243px;background:var(--green);border-top:3px solid var(--charcoal)}
.welcome-kicker{left:37px;top:517px;font-size:23px;color:#444}
.welcome-title{left:37px;top:550px;font-size:23px;color:#fff;white-space:nowrap}
.welcome-lead{left:34px;top:584px;width:580px;font-size:16.5px;line-height:24px;color:#fff}
.welcome-body{left:34px;top:656px;width:580px;font-size:12.3px;line-height:20px;color:#fff}
.courses-box{left:642px;top:527px;width:303px;height:171px;background:var(--green-panel);box-shadow:0 1px 3px rgba(0,0,0,.35);padding:20px 28px}
.courses-box h2{font-family:"Sniglet",sans-serif;font-weight:800;font-size:19px;color:#fff;margin-bottom:10px}
.courses-box li{list-style:none;font-family:"Sniglet",sans-serif;font-weight:800;font-size:18px;color:#fff;display:flex;align-items:center;gap:14px;height:30px;padding-left:8px}

/* lower columns */
.col-title{top:760px;font-size:18px;color:#333}
.news{left:32px;top:795px;width:284px}
.news-item{padding:0 2px 12px}
.news-item + .news-item{border-top:1px solid var(--line);padding-top:12px;margin-top:10px}
.news-head{font-size:12px;letter-spacing:.6px;line-height:18px;color:#333;padding-left:4px}
.news-date{font-size:14px;font-weight:700;color:var(--green-bright);margin:10px 0 8px 4px}
.news-text{font-size:12px;line-height:19px;color:#333;letter-spacing:-.1px}
.feed-title{left:370px;display:flex;align-items:center;gap:10px}
.feed-dot{width:14px;height:14px;border-radius:50%;background:var(--green-bright)}
.feed-box{left:361px;top:793px;width:266px;height:206px;background:#f5f6f5;border:1px solid #ccc;border-radius:3px;padding:14px 16px;font-size:12.5px}
.feed-post{margin-bottom:22px;line-height:18px}
.feed-post b{font-weight:400}
.feed-post time{display:block;margin-top:10px;color:#444}
.social-row{left:361px;top:1028px;display:flex;align-items:center;gap:12px;font-size:11.5px;color:#444}
.social-name{font-size:13px;color:var(--ink)}
.like-btn{border:1px solid #c6c6c6;background:#f3f3f3;color:#444;font-size:11px;padding:2px 6px;border-radius:2px}
.quote{left:663px;top:795px;width:303px;height:88px;background:#f5f5f5;box-shadow:0 1px 3px rgba(0,0,0,.3);padding:12px 20px 0 28px;font-size:12.5px;font-style:italic;line-height:18px;text-align:justify;color:#444}
.newsletter{left:663px;top:907px;width:303px;height:140px;background:var(--green-pale);border:1px solid var(--green-pale-border);box-shadow:0 1px 3px rgba(0,0,0,.2);padding:14px 11px}
.newsletter h2{font-size:18px;font-weight:700;color:var(--green);margin-bottom:10px;white-space:nowrap}
.newsletter .field{height:32px;background:#fff;border:1px solid #c9c9c9;border-radius:2px;font-size:15px;color:#c2c2c2;padding:5px 6px}
.newsletter .submit{margin:12px 0 0 3px;width:83px;height:34px;background:var(--green-bright);color:#fff;font-size:17px;border-radius:2px;display:flex;align-items:center;justify-content:center;box-shadow:1px 1px 2px rgba(0,0,0,.35)}

/* footer */
.site-footer{left:0;top:1069px;width:1000px;height:64px;background:var(--charcoal);color:#fff}
.footer-nav{position:absolute;left:37px;top:12px;font-size:13px;display:flex;gap:13px}
.copyright{position:absolute;left:41px;top:43px;font-size:10px}
.footer-social{position:absolute;right:82px;top:20px;display:flex;align-items:center;gap:14px;font-size:13px}
.footer-social .sep{width:1px;height:40px;background:#6a6464}
</style>
</head>
<body>
<div class="page">

  <header>
    <div class="abs brand"><span class="brand-mark"></span><span class="brand-name">Brindle Learning</span></div>

    <div class="abs contact contact-phone">
      <svg width="22" height="22" viewBox="0 0 22 22"><path d="M6 2c-2 1-3 3-2 6 2 5 5 9 10 11 2 1 4 0 5-2l-3-3-2 1c-2-1-4-4-5-6l1-2z" fill="#222"/><rect x="3" y="18" width="14" height="3" fill="#222"/></svg>
      <span>(02) 5550 3184</span>
    </div>
    <div class="abs contact contact-mail">
      <svg width="26" height="18" viewBox="0 0 26 18"><rect x="1" y="1" width="24" height="16" fill="none" stroke="#222" stroke-width="2"/><path d="M1 1l12 9 12-9M1 17l9-8M25 17l-9-8" fill="none" stroke="#222" stroke-width="2"/></svg>
      <span>learn@brindlelearning.com.au</span>
    </div>

    <div class="abs search">
      <div class="search-field">
        <svg width="20" height="20" viewBox="0 0 20 20"><circle cx="8" cy="8" r="6" fill="none" stroke="#c8c8c8" stroke-width="2.5"/><path d="M12 12l6 6" stroke="#c8c8c8" stroke-width="3"/></svg>
        <span>Search</span>
      </div>
      <div class="search-button">Search</div>
    </div>

    <nav class="abs main-nav">
      <a href="#" style="width:105px" aria-label="Home">
        <svg width="26" height="24" viewBox="0 0 26 24"><path d="M2 12L13 2l11 10M6 9v13h5v-7h4v7h5V9" fill="none" stroke="#fff" stroke-width="2.4" stroke-linejoin="round"/></svg>
      </a>
      <a href="#" style="width:120px">About us</a>
      <a href="#" style="width:98px">Courses</a>
      <a href="#" style="width:101px">Inspired</a>
      <a href="#" style="width:88px">Inspire</a>
      <a href="#" style="width:122px">Contact us</a>
    </nav>
  </header>

  <section>
    <div class="abs hero-photo" role="img" aria-label="Photo of a tutor helping a student write at a classroom desk"></div>
    <p class="abs tagline">Inspiring mind + Nurturing potential =</p>
    <h1 class="abs headline">Equipping success</h1>
    <a class="abs btn btn-courses" href="#">View our courses
      <svg width="18" height="18" viewBox="0 0 18 18"><circle cx="9" cy="9" r="8" fill="#fff"/><path d="M5 9h7M9 5l4 4-4 4" fill="none" stroke="#4fae0c" stroke-width="2.2"/></svg>
    </a>
    <a class="abs btn btn-trial" href="#">Ask for free trail lesson
      <span class="divider"><svg width="16" height="12" viewBox="0 0 16 12"><path d="M1 6h13M9 1l5 5-5 5" fill="none" stroke="#333" stroke-width="1.8"/></svg></span>
    </a>
  </section>

  <section>
    <div class="abs welcome-band"></div>
    <p class="abs welcome-kicker">Welcome</p>
    <h2 class="abs welcome-title">Real HSC coaching &amp; mentoring</h2>
    <p class="abs welcome-lead">Brindle Learning are HSC mentors and tutors who aim to build real relationships and offer you the help you need. HSC tutoring is different at Brindle – in a good way.</p>
    <p class="abs welcome-body">The HSC help you need, in the years you need it. We offer small classes, individualised attention and genuine care for each student. It's different - in a good way. Feel free to find out more about us, and let us know if there's any way we can help you on your journey.</p>
    <div class="abs courses-box">
      <h2>Courses we offer</h2>
      <ul>
        <li><svg width="12" height="10" viewBox="0 0 12 10"><path d="M1 5l3 4 7-8" fill="none" stroke="#2f5e0c" stroke-width="2"/></svg>Maths</li>
        <li><svg width="12" height="10" viewBox="0 0 12 10"><path d="M1 5l3 4 7-8" fill="none" stroke="#2f5e0c" stroke-width="2"/></svg>Science</li>
        <li><svg width="12" height="10" viewBox="0 0 12 10"><path d="M1 5l3 4 7-8" fill="none" stroke="#2f5e0c" stroke-width="2"/></svg>English</li>
      </ul>
    </div>
  </section>

  <section>
    <h3 class="abs col-title" style="left:35px">News and Events</h3>
    <div class="abs news">
      <article class="news-item">
        <p class="news-head">LOREM IPSUM DOLOR SIT CONSECTETUER ADIPISCING ELIT.</p>
        <p class="news-date">1 - 4 - 2013</p>
        <p class="news-text">Consectetuer adipiscing elit, sed diam nonummy nibh euismod tincidunt ut laoreet dolore magna</p>
      </article>
      <article class="news-item">
        <p class="news-head">LOREM IPSUM DOLOR SIT CONSECTETUER ADIPISCING ELIT.</p>
        <p class="news-date">1 - 4 - 2013</p>
        <p class="news-text">Consectetuer adipiscing elit, sed diam nonummy nibh euismod tincidunt ut laoreet dolore magna</p>
      </article>
    </div>

    <h3 class="abs col-title feed-title"><span class="feed-dot"></span>Latest Flit</h3>
    <div class="abs feed-box">
      <div class="feed-post"><b>@mira&nbsp; Flitter fall last night</b><br>Thought you were<time>3 hrs ago</time></div>
      <div class="feed-post"><b>@mira&nbsp; Flitter fall last night</b><br>Thought you were<time>3 hrs ago</time></div>
    </div>
    <div class="abs social-row">
      <span class="social-name">Chatterbook</span>
      <span class="like-btn">Like</span>
      <span>100 people like this</span>
    </div>

    <h3 class="abs col-title" style="left:671px">Our Students say</h3>
    <blockquote class="abs quote">“Consectetuer adipiscing elit, sed diam nonummy nibh euismod tincidunt ut laoreet dolore magna”</blockquote>
    <div class="abs newsletter">
      <h2>Subscribe for the Newsletter</h2>
      <div class="field">Email id</div>
      <div class="submit">Submit</div>
    </div>
  </section>

  <footer class="abs site-footer">
    <nav class="footer-nav"><span>Home</span>|<span>About us</span>|<span>Courses</span>|<span>Inspired</span>|<span>Inspire</span>|<span>Contact us</span></nav>
    <p class="copyright">Copyright 2013 Brindle Learning. All rights reserved.</p>
    <div class="footer-social"><span>Chatterbook</span><span class="sep"></span><span>Flitter</span></div>
  </footer>

</div>
</body>
</html>
```